Wine Label for New exciting wine company

We require a label thats quirky and stands out in the crowded shelves of liquor stores. We are happy to use such colours as burnt orange, reds etc, or we are opened to any new brave designs with designers choice of colours. Label not to be to busy, but must have a presence. Label size to be approx 9cm Width and 10cm Long.
By the way the name of the wine ladel is Tallowbark Wines. The word Wines does not need to show on the label

Thanks
Rod Pettiford

Hi Everyone, we had a label we started a few years back called Hammockbay Wines which was a very successful wine and is still being sold today. It was fun and funky and stood out on the shelf, and thats the sort of label we wanted designed. It can be along different lines but the concept is what we are looking at.
Please go to their site www.hammockbaywines.com.au and have a look at the label.
Saying that a couple of the sesigns that have come through have merit and will still be considered.
Thanks fot all your designs so far
Rod Pettiford

```html
<!DOCTYPE html>
<html lang="en">
<head>
<meta charset="utf-8">
<title>Tallowbark Wines – 2007 Cabernet Merlot</title>
<link rel="stylesheet" href="https://fonts.googleapis.com/css2?family=Montserrat:wght@700&family=Fira+Sans+Condensed:wght@400;500&display=swap">
<style>
  :root {
    --paper: #ffffff;
    --label-black: #000000;
    --band-red: #ff0000;
    --ink-white: #ffffff;
  }
  * { margin: 0; padding: 0; box-sizing: border-box; }
  html, body {
    width: 1087px;
    height: 1200px;
    overflow: hidden;
    background: var(--paper);
  }
  .label {
    position: absolute;
    left: 21px;
    top: 17px;
    width: 1045px;
    height: 1163px;
    background: var(--label-black);
  }
  .brand-band {
    position: absolute;
    left: 0;
    top: 0;
    width: 1045px;
    height: 1163px;
  }
  .brand-name {
    font-family: "Fira Sans Condensed", sans-serif;
    font-weight: 500;
  }
  .range-name {
    position: absolute;
    left: 0;
    top: 1034px;
    width: 100%;
    text-align: center;
    color: var(--ink-white);
    font-family: "Montserrat", sans-serif;
    font-weight: 700;
    font-size: 29px;
    letter-spacing: 0.42em;
    padding-left: 0.42em;
  }
  .region {
    position: absolute;
    left: 0;
    top: 1090px;
    width: 100%;
    text-align: center;
    color: var(--ink-white);
    font-family: "Fira Sans Condensed", sans-serif;
    font-weight: 500;
    font-size: 16px;
    letter-spacing: 0.01em;
  }
  .vintage {
    position: absolute;
    left: 0;
    top: 1115px;
    width: 100%;
    text-align: center;
    color: var(--ink-white);
    font-family: "Fira Sans Condensed", sans-serif;
    font-weight: 400;
    font-size: 22px;
  }
</style>
</head>
<body>
  <main class="label">
    <svg class="brand-band" viewBox="0 0 1045 1163" width="1045" height="1163">
      <rect class="band" x="470" y="0" width="109" height="1018" fill="var(--band-red)"/>
      <text class="brand-name" transform="translate(538 760) rotate(-90)"
            font-size="40" fill="var(--ink-white)" text-anchor="middle"
            textLength="360" lengthAdjust="spacing">TALLOWBARK</text>
    </svg>
    <p class="range-name">WINES</p>
    <p class="region">MARGARET RIVER, SOUTHWEST AUSTRALIA</p>
    <p class="vintage">2007 CABERNET MERLOT</p>
  </main>
</body>
</html>
```